Tri-Fold Behavioral Health (Addiction) Agency Brochure

We need an updated and refreshed brochure design for our Residential Treatment Facilities. These facilities provide residential comprehensive treatment for those struggling with drug and alcohol addiction along with those who are dually diagnosed with mental health issues as well. We are starting with this brochure but plan to have our other brochures "match" the design and will submit that following completion of this design. I have attached a "Brochure Areas" document that is numbered and corresponds to the brochure areas of our current brochure. We have modified the wording in each of these areas so the wording in the attached word document is what needs to go on the design (not the words in the attached pictures of our current brochure). We want something that is a professional design look. The front page of the brochure needs to have our main agency Logo/Name: Maple Hollow Behavioral Health Partners (logo attached). The back page we would like to have the two locations listed with the address (possible map if able). The first is called: The Harbor at Maple Hollow - located at 7214 Tolliver Lane, Frazeysburg OH 43829. The Second Facility is called: The Brennick at Maple Hollow - located at 618 Garvin St, Zanesville OH 43708. I have also attached some pictures of our facilities that can be used. They all don't have to be used and we would still like some stock photos of "people" or group counseling, etc.

Requirements
Must have
• Need final design file to be publisher or word along with pdf and or other print type file.
Nice to have
• I have also attached the current booth design photo that we are using to possibly match design look.

```html
<!DOCTYPE html>
<html lang="en">
<head>
<meta charset="utf-8">
<title>Residential Treatment Brochure – Inside Panels</title>
<link href="https://fonts.googleapis.com/css2?family=Montserrat:wght@700;800&family=Pathway+Gothic+One&display=swap" rel="stylesheet">
<style>
  :root {
    --green: #3e7a38;
    --green-dark: #2f6a2c;
    --sky: #12a7e6;
    --bullet: #1ea0dc;
    --ink: #1f1f1f;
    --white: #ffffff;
    --slate-1: #2a7f9c;
    --slate-2: #23434f;
    --slate-3: #2d3a40;
  }
  * { margin: 0; padding: 0; box-sizing: border-box; }
  html, body { width: 1200px; height: 927px; overflow: hidden; background: var(--white); }
  body { position: relative; font-family: "Pathway Gothic One", "Arial Narrow", sans-serif; }

  .panel { position: absolute; top: 0; width: 400px; height: 927px; overflow: hidden; }
  .panel--experience { left: 0; }
  .panel--dual { left: 400px; }
  .panel--programming { left: 800px; }

  .heading {
    font-family: "Montserrat", sans-serif;
    font-weight: 800;
    letter-spacing: -1.5px;
    line-height: 0.98;
  }
  .body-copy { font-size: 18.5px; line-height: 27.2px; }

  /* Experience panel */
  .experience-photo {
    position: absolute; inset: 0;
    background: linear-gradient(160deg, var(--slate-1) 0%, #1f6a84 35%, var(--slate-2) 65%, var(--slate-3) 100%);
  }
  .experience-content { position: absolute; left: 37px; top: 420px; width: 330px; color: var(--white); }
  .experience-content .heading { font-size: 46px; margin-bottom: 32px; }
  .experience-content p + p { margin-top: 27px; }

  /* Dual diagnosis panel */
  .dual-box {
    position: absolute; left: 0; top: 0; width: 399px; height: 397px;
    background: var(--green); color: var(--white);
    padding: 30px 30px 0 36px;
  }
  .dual-box .heading { font-size: 45px; margin-bottom: 26px; }
  .garden-photo {
    position: absolute; left: 0; top: 412px; width: 399px; height: 515px;
    background: linear-gradient(180deg, #3f5a2c 0%, #51703a 40%, #6b6a52 75%, #5a4a3a 100%);
  }

  /* Programming panel */
  .programming-content { position: absolute; left: 38px; top: 34px; width: 340px; color: var(--ink); }
  .programming-content .heading { font-size: 46px; color: var(--green-dark); line-height: 1.02; margin-bottom: 26px; }
  .program-list { position: absolute; left: 38px; top: 343px; display: flex; gap: 28px; }
  .program-list ul { list-style: none; font-size: 18.5px; line-height: 27.2px; color: var(--ink); }
  .program-list ul:first-child { width: 145px; }
  .program-list li { position: relative; padding-left: 18px; }
  .program-list li::before {
    content: ""; position: absolute; left: 1px; top: 11px;
    width: 4px; height: 4px; border-radius: 50%; background: var(--bullet);
  }
  .accent-band { position: absolute; left: 0; top: 640px; width: 400px; height: 13px; background: var(--sky); }
  .group-photo {
    position: absolute; left: 0; top: 653px; width: 400px; height: 274px;
    background: linear-gradient(135deg, #3b4a2a 0%, #55603a 45%, #8a6a52 70%, #3f4b2c 100%);
  }
</style>
</head>
<body>
  <section class="panel panel--experience">
    <div class="experience-photo" role="img" aria-label="Smiling woman looking upward, blue-toned portrait"></div>
    <div class="experience-content">
      <h2 class="heading">The<br>Experience</h2>
      <p class="body-copy">Residential Treatment at Maple Hollow offers intensive structured treatment services for men and women suffering from substance abuse disorders in a 24-hour medically monitored Long-term residential treatment facility.</p>
      <p class="body-copy">Our treatment facilities offer clients the ability to feel welcomed, accepted and supported in a retreat like setting. Our multi-disciplinary team consists of Physicians, Therapists, Nurses, Case Managers, and other Recovery Support Specialists, allowing for each individual’s physical, social, mental, and emotional development.</p>
    </div>
  </section>

  <section class="panel panel--dual">
    <div class="dual-box">
      <h2 class="heading">Dual Diagnosis</h2>
      <p class="body-copy">It is an unfortunate reality that many individuals who struggle with addiction are also faced with mental illness. Our residential treatment programs support dually-diagnosed individuals by providing onsite psychiatric evaluations, regular psychiatric follow-ups, medication management, and therapy services aimed at treating these symptoms as a part of the client’s individualized treatment plan.</p>
    </div>
    <div class="garden-photo" role="img" aria-label="Stone garden path beneath an arch of hanging ivy, with stacked pumpkins"></div>
  </section>

  <section class="panel panel--programming">
    <div class="programming-content">
      <h2 class="heading">Our<br>Programming</h2>
      <p class="body-copy">Residential treatment programing provides comprehensive treatment for those struggling with drug and alcohol addiction along with those who are dually diagnosed with mental health issues as well. Residents will be able to experience an evidence-based program model inclusive of:</p>
    </div>
    <div class="program-list">
      <ul>
        <li>Comprehensive Evaluations</li>
        <li>Treatment Team Collaboration</li>
        <li>Medication Management</li>
        <li>Aftercare Planning</li>
        <li>Individual Therapy</li>
        <li>Family Therapy</li>
        <li>Group Therapy Groups</li>
      </ul>
      <ul>
        <li>Psychoeducational</li>
        <li>Psychotherapy</li>
        <li>Health &amp; Wellness</li>
        <li>Independent Living Skills</li>
        <li>Peer-Led (AA/NA)</li>
        <li>Grief &amp; Loss</li>
        <li>Codependency</li>
        <li>Stress Management</li>
      </ul>
    </div>
    <div class="accent-band"></div>
    <div class="group-photo" role="img" aria-label="Group of hands joined together in a circle over grass"></div>
  </section>
</body>
</html>
```